Rancho Brisolo Wine Bottle Label

Hello! We are looking for a wine bottle label design for our private, family winery located in Chico, CA. The name of our home/ranch/vineyard is Rancho Brisolo ('the exit'), which is inspired by our hilltop location, panoramic views of the valley, and sensation of escaping from the busy world below.

We planted our vineyard in 2011 and are now bottling our first harvest from fall of 2013. We planted all Italian varietals on our land: syrah, primitivo, and montepulciano. The wine we make is the culmination of all the love, support and effort poured into the process by our family and friends.

The task at hand: we are looking for a clean, simple front and back wine label design.

Front Label Content:
RB and/or Rancho Brisolo
Estate Grown
Chico, CA
Varietal (use Syrah for placeholder)
Year (use 2013 for placeholder)

Back Label Content:
Running list of names of all family and friends who have participated in the process (use a text fill for placeholder)

Aesthetic Description:
Simple, clean, contemporary, text based design (see attached logo idea, Image #1)
Like the brown paper with stamped lettering look & feel
Like the classic clear label with gold lettering look & feel
Option to incorporated a simple background image/sketch of the view overlooking the valley (see attached Image #2 and #3)
Additional inspirational images attached for reference (Images #3- )

General Size Requirement:
Front Label - 4"tall by 3 1/2" wide
Back Label - 4"tall by 3 1/2" wide

Format:
Please submit Photoshop or Illustrator or InDesign Files and PDF/EPS Files.

Industry/Entity Type

Ranch

```html
<!DOCTYPE html>
<html lang="en">
<head>
<meta charset="utf-8">
<title>Rancho Brisolo — Syrah 2013 Labels</title>
<link rel="stylesheet" href="https://fonts.googleapis.com/css2?family=Ubuntu:wght@400;500&display=swap">
<style>
  :root {
    --backdrop-light: #f2f2f2;
    --backdrop-dark: #c9c9c9;
    --gold: #f2c46c;
    --gold-deep: #e0962a;
    --gold-edge: #f0a93a;
    --paper: #f4efe4;
    --brown: #5a2a0c;
    --brown-dark: #3e1a06;
    --capsule-light: #f9bb4c;
    --capsule-dark: #e8922a;
    --capsule-ink: #c2620f;
    --mark-grey: #8c8c8c;
  }
  * { box-sizing: border-box; margin: 0; padding: 0; }
  html, body { width: 1200px; height: 947px; overflow: hidden; }
  body {
    position: relative;
    font-family: "Ubuntu", sans-serif;
    background: radial-gradient(ellipse at 50% 30%, var(--backdrop-light) 0%, #e2e2e2 55%, var(--backdrop-dark) 100%);
  }

  .capsule-label {
    position: absolute; left: 162px; top: 66px; width: 194px; height: 166px;
    background: linear-gradient(135deg, var(--capsule-dark) 0%, var(--capsule-light) 45%, var(--capsule-dark) 100%);
    color: var(--capsule-ink);
    text-align: center;
  }
  .capsule-label .monogram { font-size: 44px; font-weight: 500; line-height: 1; margin-top: 62px; }
  .capsule-label .varietal-year { font-size: 23px; letter-spacing: 1px; margin-top: 10px; }

  .corner-mark {
    position: absolute; right: 18px; top: 24px; width: 180px;
    text-align: center; color: var(--mark-grey);
  }
  .corner-mark .monogram { font-size: 52px; font-weight: 500; line-height: 1; }
  .corner-mark .varietal-year { font-size: 22px; letter-spacing: 1px; margin-top: 4px; }

  .label {
    position: absolute; top: 417px; width: 376px; height: 328px;
    border: 3px solid var(--gold-edge);
    background: var(--paper);
    padding: 13px;
  }
  .label--front { left: 72px; }
  .label--back { left: 748px; }
  .label__frame {
    position: relative; width: 100%; height: 100%;
    border: 4px solid var(--gold-edge);
    overflow: hidden;
  }
  .label__ground {
    position: absolute; inset: 0;
    background: linear-gradient(180deg, var(--brown) 0%, #5f2d0e 55%, var(--brown-dark) 100%);
  }
  .label__content {
    position: relative; height: 100%;
    text-align: center; color: var(--gold);
  }

  .label--front .monogram { font-size: 150px; font-weight: 500; line-height: 1; padding-top: 8px; letter-spacing: -4px; }
  .label--front .estate-name { font-size: 25px; margin-top: 6px; }
  .label--front .vintage { font-size: 36px; margin-top: 6px; line-height: 1.1; }
  .label--front .varietal { font-size: 37px; font-weight: 500; line-height: 1.1; margin-top: 4px; }

  .label--back .credits {
    padding: 16px 30px 0;
    font-size: 20.5px; line-height: 28.5px;
  }
</style>
</head>
<body>

  <section class="capsule-label" aria-label="Capsule label">
    <div class="monogram">RB</div>
    <div class="varietal-year">SYRAH 2013</div>
  </section>

  <section class="corner-mark" aria-label="Wine mark">
    <div class="monogram">RB</div>
    <div class="varietal-year">SYRAH 2013</div>
  </section>

  <section class="label label--front" aria-label="Front label">
    <div class="label__frame">
      <div class="label__ground" role="img" aria-label="Faint sketch of vineyard rows overlooking the valley"></div>
      <div class="label__content">
        <div class="monogram">RB</div>
        <div class="estate-name">Rancho Brisolo</div>
        <div class="vintage">2013</div>
        <div class="varietal">SYRAH</div>
      </div>
    </div>
  </section>

  <section class="label label--back" aria-label="Back label">
    <div class="label__frame">
      <div class="label__ground" role="img" aria-label="Faint sketch of vineyard rows overlooking the valley"></div>
      <div class="label__content">
        <p class="credits">Lorem ipsum dolor sit amet, consectetur adipiscing elit, sed do eiusmod tempor incididunt ut labore et dolore magna aliqua. Ut enim ad minim veniam, quis nostrud exercitation</p>
      </div>
    </div>
  </section>

</body>
</html>
```